Unique Private Wine Label for Wine Bottles (UPDATED BRIEF)

Updated Brief Oct 15, 2017. Please see below!

I am looking for a unique wine label designs for my wine bottles. I create wine and would like to have wine labels for my bottles. I am looking for a main label and then several additional labels with the same design just with the type of wine listed on the label (see below for wine types). This is private wine for family and friends to consume not commercially produced wine.

I would like a rustic, classic or vintage design with some color in the label. I do have a specific name for the wine which i like to call "Fernhollow" . I would like to see different designs.

We would like vintage or classic labels. Please give me a few multiple designs based on above. I also want to have a main label and then incorporate different types of wine into the labels like "Chardonnay" or "Pinot Noir" or "Sauvignon Blanc" or "Caberent Savignon" or "Merlot" below the name of the wine. As an example, the labels will be the same design but the word Sauvignon Blanc will be incorporated into the design for this type of wine label and so on for the other types of wine.

Please let me know if you have any questions.

Reason: I Have changed the vision of the design. I would like a classic, rustic or vintage design NOT a beach theme. The brief has been updated as of Oct 15, 2017. Please see updated brief for instructions on new design

Note: I have changed the vision of the design. I would like a classic, rustic or vintage design NOT a beach theme. The brief has been updated as of Oct 15, 2017. Please see updated brief for instructions on new design. I would like new designers to provide new designs! Payment is Guaranteed! Thanks!

Target Market(s)

This is private wine for family and friends to consume not commercially produced wine.

Font styles to use
Decorative
Script

Colors

Designer to choose colors to be used in the design.

Requirements
Must have
• Updated Brief Oct 15, 2017. Please see below!
• I am looking for a unique wine label designs for my wine bottles. I create wine and would like to have wine labels for my bottles. I am looking for a main label and then several additional labels with the same design just with the type of wine listed on the label (see below for wine types). This is private wine for family and friends to consume not commercially produced wine.
• I would like a rustic, classic or vintage design with some color in the label. I do have a specific name for the wine which i like to call "Fernhollow". I would like to see different designs.
• We would like vintage or classic labels. Please give me a few multiple designs based on above. I also want to have a main label and then incorporate different types of wine into the labels like "Chardonnay" or "Pinot Noir" or "Sauvignon Blanc" or "Caberent Savignon" or "Merlot" below the name of the wine. As an example, the labels will be the same design but the word Sauvignon Blanc will be incorporated into the design for this type of wine label and so on for the other types of wine.
• Please let me know if you have any questions.
Nice to have
Should not have
• Please see the updated brief instructions above. I DO NOT WANT A BEACH THEME ANYMORE!

```html
<!DOCTYPE html>
<html lang="en">
<head>
<meta charset="utf-8">
<title>Fernhollow Wines – Back Label</title>
<link rel="stylesheet" href="https://fonts.googleapis.com/css2?family=Cinzel:wght@400;500&family=Montserrat:wght@500;700&display=swap">
<style>
  :root {
    --backdrop: #1b1b1b;
    --paper-light: #f6f1d9;
    --paper-mid: #eee6c6;
    --paper-edge: #e0d6ad;
    --paper-fleck: #b9a978;
    --ink: #3b352b;
    --ink-dark: #221e18;
  }
  * { margin: 0; padding: 0; box-sizing: border-box; }
  html, body {
    width: 1200px;
    height: 686px;
    overflow: hidden;
    background: var(--backdrop);
  }
  .canvas {
    position: relative;
    width: 1200px;
    height: 686px;
    background: var(--backdrop);
  }
  .back-label {
    position: absolute;
    left: 480px;
    top: 209.6px;
    width: 241.6px;
    height: 268.8px;
    overflow: hidden;
    background: radial-gradient(ellipse at 50% 45%, var(--paper-light) 0%, var(--paper-mid) 70%, var(--paper-edge) 100%);
    color: var(--ink);
  }
  .paper-texture {
    position: absolute;
    inset: 0;
    width: 100%;
    height: 100%;
  }
  .label-content {
    position: relative;
    padding: 18px 30.6px 0 31px;
  }
  .story {
    font-family: "Cinzel", serif;
    font-size: 11.3px;
    line-height: 12.6px;
    text-transform: uppercase;
    color: var(--ink);
  }
  .story-line {
    display: block;
    white-space: nowrap;
    text-align: justify;
    text-align-last: justify;
  }
  .story-line.is-last { text-align-last: center; }
  .producer {
    margin-top: 9px;
    text-align: center;
    font-family: "Cinzel", serif;
    color: var(--ink-dark);
  }
  .producer-line {
    font-size: 8.4px;
    line-height: 11px;
    text-transform: uppercase;
  }
  .producer-name {
    font-size: 12.2px;
    line-height: 14px;
  }
  .government-warning {
    margin-top: 8px;
    font-family: "Montserrat", sans-serif;
    font-weight: 500;
    font-size: 6.2px;
    line-height: 7.85px;
    letter-spacing: 0.45px;
    text-transform: uppercase;
    color: var(--ink-dark);
  }
  .warning-line { display: block; white-space: nowrap; }
  .government-warning strong { font-weight: 700; }
  .sulfites {
    margin-top: 7px;
    text-align: center;
    font-family: "Montserrat", sans-serif;
    font-weight: 700;
    font-size: 6.4px;
    letter-spacing: 0.5px;
    text-transform: uppercase;
    color: var(--ink-dark);
  }
</style>
</head>
<body>
<main class="canvas">
  <section class="back-label">
    <svg class="paper-texture" viewBox="0 0 242 269" preserveAspectRatio="none" aria-hidden="true">
      <defs>
        <filter id="paper-grain" x="0" y="0" width="100%" height="100%">
          <feTurbulence type="fractalNoise" baseFrequency="0.035 0.05" numOctaves="4" seed="7" result="mottle"/>
          <feColorMatrix in="mottle" type="matrix"
            values="0 0 0 0 0.72
                    0 0 0 0 0.66
                    0 0 0 0 0.47
                    0 0 0 1.1 -0.45"/>
        </filter>
        <filter id="paper-fibre" x="0" y="0" width="100%" height="100%">
          <feTurbulence type="fractalNoise" baseFrequency="0.9" numOctaves="2" seed="3" result="fibre"/>
          <feColorMatrix in="fibre" type="matrix"
            values="0 0 0 0 0.6
                    0 0 0 0 0.55
                    0 0 0 0 0.4
                    0 0 0 0.9 -0.38"/>
        </filter>
        <radialGradient id="paper-vignette" cx="50%" cy="48%" r="70%">
          <stop offset="60%" stop-color="#c9bb8a" stop-opacity="0"/>
          <stop offset="100%" stop-color="#c9bb8a" stop-opacity="0.35"/>
        </radialGradient>
      </defs>
      <rect width="242" height="269" filter="url(#paper-grain)" opacity="0.55"/>
      <rect width="242" height="269" filter="url(#paper-fibre)" opacity="0.35"/>
      <rect width="242" height="269" fill="url(#paper-vignette)"/>
    </svg>
    <div class="label-content">
      <p class="story">
        <span class="story-line">Fernhollow wines resides in</span>
        <span class="story-line">the coastal town of old</span>
        <span class="story-line">Saltmarsh, connecticut</span>
        <span class="story-line">where Matteo Lorenzini</span>
        <span class="story-line">hand crafts the finest</span>
        <span class="story-line">italian inspired wines.</span>
        <span class="story-line">Fernhollow wines produces</span>
        <span class="story-line">quality red and white</span>
        <span class="story-line is-last">wines on premise.</span>
      </p>
      <div class="producer">
        <p class="producer-line">Vinted &amp; bottled by</p>
        <p class="producer-name">Fernhollow Wines</p>
      </div>
      <p class="government-warning">
        <span class="warning-line"><strong>Government warning</strong>: (1) according to</span>
        <span class="warning-line">the surgeon general, women should</span>
        <span class="warning-line">not drink alcoholic beverages</span>
        <span class="warning-line">during pregnancy because of the</span>
        <span class="warning-line">risk of birth defects. (2) consump-</span>
        <span class="warning-line">tion of alcoholic beverages impairs</span>
        <span class="warning-line">your ability to drive a car or oper-</span>
        <span class="warning-line">ate machinery, and may cause health</span>
        <span class="warning-line">problems.</span>
      </p>
      <p class="sulfites">Contains sulfites</p>
    </div>
  </section>
</main>
</body>
</html>
```